FULLY CUSTOM MAIN BANNER IMAGE FOR MY WEBSITE-REDESIGN CURRENT

SIZE MUST BE: 1800x829

LOOKING FOR A FULLY CUSTOM MAIN BANNER IMAGE TO BE DESIGNED FOR MY NEW WEBSITE HOMEPAGE http://pixelquarry-demo.net/qa/dorin/vtl_draft/index.html THE CONTENT THAT YOU SEE ON THE UPLOADED FILE OR HERE http://pixelquarry-demo.net/qa/dorin/vtl_draft/index.html YOU CAN SEE MY EXISTING BANNER IMAGE...IS THE SAME CONTENT I WANT ON THE CUSTOM BANNER IMAGE BUT I WANT THE BANNER IMAGE TO USE IMAGES TO PORTRAY WHAT THE CONTENT SAYS. POSSIBLE INTEGRATE AN INFOGRAPHIC DESIGN IN THE BANNER IMAGE. IM OPEN TO ALL IDEAS.

WHEN SOMEONE GOES TO MY WEBSITE, IMMEDIATELY I WANT THEM TO UNDERSTAND WHAT IT IS I DO.

MY BUSINESS PROVIDES OTHER BUSINESSES WITH THE ABILITY TO CREATE PROMOTIONAL GIVEAWAYS AND MARKETING PROMOTIONS USING GIFT VOUCHERS THAT ARE REDEEMABLE FOR FREE VACATIONS, CRUISES, ALL INCLUSIVE RESORT STAYS, TABLETS, SMARTWATCHES, DINING AND RESTAURANT INCENTIVES AND REWARDS AND MORE.

CURRENTLY THE CONTENT ON THE BANNER IMAGE IS THIS:
BOOST SALES & LEADS OVERNIGHT
BY ENTICING YOUR CUSTOMERS WITH FREE VACATION CERTIFICATES & OTHER HIGH PERCEIVED VALUE INCENTIVES

I HAVE ATTACHED A DOCUMENT WITH IMAGE ASSETTS YOU MAY REVIEW AND USE OR GET IDEAS FROM.

THE BOTTOM LINE IS MY SERVICE HELPS BUSINESSES INCREASE LEADS, CONVERSIONS, CTA, SALES, ETC WITHOUT HAVING TO INCREASE THEIR EXISTING AD SPEND. SIMPLY BY ADDING A FREE OFFER TO ALL THEIR EXISTING ADS WILL DRAMATICALLY INCREASE RESPONSE RATES. SO I WANT THIS BANNER TO REFLECT THIS SOMEHOW....MORE CUSTOMERS USING GIVEAWAYS!

Target Market(s)

B2B, SMALL BUSINESS OWNERS, ENTREPRENEURS, SOLOPRENEURS, MARKETING AGENCIES,

Industry/Entity Type

Digital Marketing

Requirements
Must have
• MUST PORTRAY THE RED CONTENT/TEXT USING IMAGES OF MY ASSETTS AND THE PORTRAY MORE CUSTOMERS---MUST BE FULLY CUSTOM

SIZE MUST BE: 1800x829
Nice to have
• USE CONTENT IN CURRENT BANNER IMAGE ALSO MAKE SURE TO USE THE FREE SAMPLE PKG BUTTON TOO.....MUST BE FULLY CUSTOM

SIZE MUST BE: 1800x829
Should not have
• MUST BE FULLY CUSTOM

SIZE MUST BE: 1800x829

```html
<!DOCTYPE html>
<html lang="en">
<head>
<meta charset="utf-8">
<title>Boost Sales &amp; Leads Overnight</title>
<link rel="stylesheet" href="https://fonts.googleapis.com/css2?family=Oswald:wght@500;600&family=Pathway+Gothic+One&family=Montserrat:wght@300;800&display=swap">
<style>
  :root {
    --sky-top: #34302f;
    --sky-warm: #6e4a33;
    --sky-glow: #8a5a38;
    --sea-dark: #262b31;
    --gold: #f7bf4f;
    --white: #ffffff;
    --band: rgba(30, 26, 26, 0.6);
    --green: #4caf50;
    --frame: #ffffff;
  }
  html, body {
    margin: 0;
    padding: 0;
    width: 1200px;
    height: 553px;
    overflow: hidden;
    background: var(--sea-dark);
  }
  .banner {
    position: relative;
    width: 1200px;
    height: 553px;
    overflow: hidden;
  }
  .banner__backdrop {
    position: absolute;
    inset: 0;
    background:
      radial-gradient(ellipse 420px 120px at 700px 330px, rgba(180, 110, 60, 0.45), transparent 70%),
      linear-gradient(180deg, var(--sky-top) 0%, #4a3a33 30%, var(--sky-warm) 52%, var(--sky-glow) 60%, #3b3535 70%, var(--sea-dark) 100%);
  }
  .banner__headline {
    position: absolute;
    left: 81px;
    top: 98px;
    margin: 0;
    font-family: "Oswald", sans-serif;
    font-weight: 600;
    font-size: 39px;
    line-height: 1;
    letter-spacing: 1.3px;
    color: var(--white);
    white-space: nowrap;
  }
  .accent { color: var(--gold); }
  .banner__subline {
    position: absolute;
    left: 0;
    width: 735px;
    top: 170px;
    margin: 0;
    text-align: center;
    font-family: "Oswald", sans-serif;
    font-weight: 500;
    font-size: 25px;
    line-height: 29.5px;
    color: var(--white);
    text-transform: uppercase;
    white-space: nowrap;
  }
  .banner__offer {
    position: absolute;
    left: 60px;
    top: 304px;
    width: 531px;
    height: 46px;
    background: linear-gradient(90deg, transparent 0, var(--band) 70px, var(--band) 100%);
    clip-path: polygon(0 0, 98% 0, 100% 100%, 0 100%);
    display: flex;
    align-items: center;
    justify-content: flex-end;
    padding-right: 30px;
    box-sizing: border-box;
    font-family: "Pathway Gothic One", sans-serif;
    font-size: 30px;
    color: var(--white);
    white-space: nowrap;
  }
  .banner__cta {
    position: absolute;
    left: 218px;
    top: 396px;
    width: 299px;
    height: 71px;
    background: var(--green);
    clip-path: polygon(0 0, 100% 0, 99% 88%, 3% 100%, 0% 88%);
    display: flex;
    flex-direction: column;
    align-items: center;
    justify-content: center;
    text-decoration: none;
    color: var(--white);
    padding-bottom: 6px;
    box-sizing: border-box;
  }
  .banner__cta-title {
    font-family: "Montserrat", sans-serif;
    font-weight: 800;
    font-size: 21px;
    letter-spacing: 0.2px;
    line-height: 1.1;
  }
  .banner__cta-note {
    font-family: "Montserrat", sans-serif;
    font-weight: 300;
    font-size: 14px;
    margin-top: 4px;
  }
  .banner__collage {
    position: absolute;
    inset: 0;
    width: 1200px;
    height: 553px;
  }
</style>
</head>
<body>
<main class="banner">
  <div class="banner__backdrop" role="img" aria-label="Dusky beach at sunset with dark sea, rocks and palm silhouettes"></div>

  <h1 class="banner__headline"><span class="accent">BOOST SALES</span> &amp; LEADS OVERNIGHT</h1>

  <p class="banner__subline">
    By enticing your customers<br>
    with <span class="accent">free</span> vacation certificates &amp;<br>
    other high perceived value incentives
  </p>

  <div class="banner__offer"><span class="accent">Get Free Samples</span>&nbsp;Now For A Limited Time !</div>

  <a class="banner__cta" href="#free-samples">
    <span class="banner__cta-title">GET FREE SAMPLES</span>
    <span class="banner__cta-note">100% FREE</span>
  </a>

  <svg class="banner__collage" viewBox="0 0 1800 829" preserveAspectRatio="none">
    <defs>
      <linearGradient id="resortTones" x1="0" y1="0" x2="1" y2="1">
        <stop offset="0" stop-color="#8fa9b2"/>
        <stop offset="0.45" stop-color="#c08a4a"/>
        <stop offset="1" stop-color="#5b4630"/>
      </linearGradient>
      <linearGradient id="poolTones" x1="0" y1="0" x2="1" y2="1">
        <stop offset="0" stop-color="#9a6a4c"/>
        <stop offset="0.5" stop-color="#5ec4dc"/>
        <stop offset="1" stop-color="#b7c9cf"/>
      </linearGradient>
      <linearGradient id="palmTones" x1="0" y1="0" x2="0" y2="1">
        <stop offset="0" stop-color="#3f8fd0"/>
        <stop offset="0.55" stop-color="#6e8f5a"/>
        <stop offset="1" stop-color="#e8e6df"/>
      </linearGradient>
      <linearGradient id="sunsetTones" x1="0" y1="0" x2="0" y2="1">
        <stop offset="0" stop-color="#b9a7c6"/>
        <stop offset="0.4" stop-color="#f08a6a"/>
        <stop offset="0.65" stop-color="#6d86a6"/>
        <stop offset="1" stop-color="#3c4a5c"/>
      </linearGradient>
    </defs>
    <g stroke="var(--frame)" stroke-width="18" stroke-linejoin="round">
      <polygon role="img" aria-label="Beachfront resort terrace with loungers, umbrellas and calm bay" fill="url(#resortTones)"
        points="1215,-20 1820,-20 1820,78 1512,380 1300,182 1185,40"/>
      <polygon role="img" aria-label="Palm trees under blue sky on a white sand beach" fill="url(#palmTones)"
        points="1820,78 1820,728 1492,410"/>
      <polygon role="img" aria-label="Cruise ship deck with blue swimming pool and sun loungers" fill="url(#poolTones)"
        points="1302,182 1512,382 1318,632 1088,410"/>
      <polygon role="img" aria-label="Pink and orange sunset over a rocky shoreline" fill="url(#sunsetTones)"
        points="1530,468 1820,748 1820,850 1220,850 1188,790 1310,650"/>
    </g>
  </svg>
</main>
</body>
</html>
```